" Trabalhamos com café, bebidas a base de café, frapuccino, sorvetes, milk-shakes, taças, bolos, tortas doces e salgadas, doces, salgados assados e sucos. "

```html
<!DOCTYPE html>
<html lang="pt-BR">
<head>
<meta charset="UTF-8">
<title>Brunetto – Peças de Identidade</title>
<link href="https://fonts.googleapis.com/css2?family=Roboto+Slab:wght@500&display=swap" rel="stylesheet">
<style>
  :root{
    --page:#ffffff;
    --stage:#7b7b7b;
    --cream-light:#fde9b8;
    --cream:#f7cf7f;
    --cream-deep:#eab45c;
    --brown-dark:#3d1f10;
    --brown:#5a301a;
    --brown-mid:#7a4526;
    --ring:#c89a6a;
    --text-dark:#3a1d0e;
    --text-light:#fbe7c4;
  }
  *{margin:0;padding:0;box-sizing:border-box}
  html,body{width:1200px;height:1200px;overflow:hidden;background:var(--page)}
  body{position:relative;font-family:"Roboto Slab",Georgia,serif}
  .stage{position:absolute;left:0;top:180px;width:1200px;height:840px;background:var(--stage)}

  .profile-tile{
    position:absolute;left:492px;top:276px;width:216px;height:216px;
    background:radial-gradient(circle at 50% 50%,var(--cream-light) 0%,var(--cream) 60%,var(--cream-deep) 100%);
    display:flex;align-items:center;justify-content:center;
  }
  .profile-tile .seal{
    width:160px;height:160px;border-radius:50%;
    background:var(--brown);border:5px solid var(--ring);
    box-shadow:0 0 0 3px var(--brown-dark);
    display:flex;align-items:center;justify-content:center;
  }
  .profile-tile .brand-name{color:var(--text-light);font-size:22px;font-weight:500;letter-spacing:1px}

  .banner{
    position:absolute;left:67px;top:540px;width:1061px;height:384px;overflow:hidden;
    background:linear-gradient(90deg,var(--brown-dark) 0%,var(--brown) 45%,var(--brown-mid) 70%,var(--brown) 100%);
  }
  .banner .menu-panel{
    position:absolute;inset:0;
    background:linear-gradient(180deg,var(--cream-light),var(--cream) 70%,var(--cream-deep));
    clip-path:polygon(0 0,420px 0,480px 100%,0 100%);
  }
  .menu-list{
    position:absolute;left:22px;top:18px;list-style:none;
    color:var(--text-dark);font-size:25px;line-height:28px;font-weight:500;letter-spacing:.5px;
  }
  .hours{
    position:absolute;left:22px;top:318px;display:flex;align-items:center;gap:10px;color:var(--text-dark);
  }
  .hours .dot{width:34px;height:34px;border-radius:50%;background:var(--brown-dark)}
  .hours p{font-size:14px;line-height:16px}
  .hours strong{font-weight:500;font-size:15px}

  .product-photo{
    position:absolute;left:270px;top:80px;width:460px;height:290px;border-radius:30px;
    background:radial-gradient(ellipse at 30% 70%,#f1e4d3 0%,#c69b6f 35%,rgba(120,70,40,.6) 65%,rgba(90,48,26,0) 90%),
               radial-gradient(ellipse at 78% 60%,#6b3a20 0%,rgba(90,48,26,0) 60%);
  }

  .banner-seal{
    position:absolute;left:680px;top:28px;width:360px;height:360px;border-radius:50%;
    background:radial-gradient(circle,var(--brown-mid) 0%,var(--brown) 60%,var(--brown-dark) 100%);
    border:8px solid var(--ring);box-shadow:0 0 0 6px var(--brown-dark);
    display:flex;align-items:center;justify-content:center;
  }
  .banner-seal .brand-name{color:var(--text-light);font-size:50px;font-weight:500;letter-spacing:2px}
</style>
</head>
<body>
  <div class="stage"></div>

  <div class="profile-tile">
    <div class="seal"><span class="brand-name">BRUNETTO</span></div>
  </div>

  <section class="banner">
    <div class="menu-panel"></div>
    <ul class="menu-list">
      <li>CAFÉ EXPRESSO</li>
      <li>CAFÉ GOURMET</li>
      <li>FRAPUCCINO</li>
      <li>SORVETES</li>
      <li>TAÇAS</li>
      <li>BOLOS</li>
      <li>TORTAS DOCES E</li>
      <li>SALGADAS</li>
      <li>ASSADOS</li>
      <li>SUCOS NATURAIS</li>
    </ul>
    <div class="hours">
      <span class="dot"></span>
      <p>De seg à Sáb<br><strong>das 08h às 17h</strong></p>
    </div>
    <div class="product-photo" role="img" aria-label="Foto de xícara de café com leite, frapuccino com chantilly e taça de sorvete de chocolate"></div>
    <div class="banner-seal"><span class="brand-name">BRUNETTO</span></div>
  </section>
</body>
</html>
```